Wedding Invitation : Who helps to design a chic wedding card?

We need a chic invitation design for our wedding invitations.

FRONT

- Name logo : Mira & Joost
- Wedding date : zaterdag 9 juli 2022
- Quote : forever starts here

BACK

- Wij geven elkaar het ja-woord op zaterdag 9 juli 2022
Translation: We’ll say yes on Saturday 9th of July 2022 in the church of Lindakker
- Timeline with icons:

o JAWOORD (Translation: We say yes)
o 15u00

o RECEPTIE (Translation: Reception)
o 18u30

o DINER (Translation: Dinner)
o 19u30
o Feestzaal Lorvendaal (Location)

o FEEST (Translation: Dinner)
o 21u30

- Locations:

o Icon of a church:
Lindakker
o Icon of a location:
Feestzaal Lorvendaal
Burgemeester Tijskenslaan 47B
9740 Oostervelde

- RSVP Gelieve jouw aanwezigheid te bevestigen voor 29 mei 2022
(Translation: Please confirm before 29th of May 2022)

STYLE:

- Rosé gold relief press symbols
- Font style : handwritten or serif name (eg. playfair display)
- Font style: description in a more minimalistic font
- Cards will be in craft or ivory white, text will be in rosé gold relief press or black print

FORMAT
American format (229mm W x 114 mm H)

Target Market(s)

People 25-40 years old

Industry/Entity Type

Wedding / Event

Font styles to use
Serif
Sans Serif
Script

Colors

Designer to choose colors to be used in the design.

Requirements
Must have
• Name logo
Nice to have
• Minimalistic animation / icons
Should not have
• Jungle prints

```html
<!DOCTYPE html>
<html lang="nl">
<head>
<meta charset="utf-8">
<title>Mira &amp; Joost – Wedding Invitation, Unfolded Option</title>
<link rel="stylesheet" href="https://fonts.googleapis.com/css2?family=Playfair+Display:wght@400;700&family=Oswald:wght@300&family=Josefin+Sans:wght@400&family=Allura&display=swap">
<style>
  :root{
    --board:#735647;
    --ivory:#eee6dd;
    --paper:#ffffff;
    --rose-gold:#b48459;
    --rose-gold-line:#c9a27b;
    --blush:#efd6c7;
    --blush-deep:#e9c7b4;
    --ink:#1d1a18;
    --label:#ecd9cc;
  }
  *{box-sizing:border-box;margin:0;padding:0}
  html,body{width:1200px;height:1000px;overflow:hidden}
  body{background:var(--board);position:relative;font-family:"Playfair Display",serif;color:var(--ink)}

  .board-label{
    position:absolute;left:110px;top:286px;width:260px;text-align:center;
    font-family:"Josefin Sans",sans-serif;font-weight:400;font-size:33px;
    letter-spacing:4px;line-height:1.6;color:var(--label)
  }

  .card{position:absolute;width:323px;height:649px;overflow:hidden}
  .card > *{position:absolute}
  .front{background:var(--ivory)}
  .back{background:var(--paper)}

  .is-main.front{left:454px;top:40px}
  .is-main.back{left:814px;top:40px}
  .is-mini{box-shadow:0 6px 14px rgba(40,25,15,.35)}
  .is-mini.back{left:8px;top:436px;transform:scale(.6) rotate(-8deg)}
  .is-mini.front{left:155px;top:396px;transform:scale(.6) rotate(3deg)}

  /* front */
  .front__waves{left:0;top:0;width:323px;height:649px}
  .front__frame{left:8px;top:8px;width:307px;height:633px;border:1px solid var(--rose-gold-line)}
  .front__welcome{left:0;width:100%;top:34px;text-align:center;font-size:10.5px;line-height:1.2;letter-spacing:1px;color:var(--rose-gold)}
  .front__names{left:0;width:100%;top:124px;text-align:center;font-family:"Oswald",sans-serif;font-weight:300;font-size:36px;letter-spacing:4px;color:var(--rose-gold)}
  .front__rule{left:142px;top:261px;width:40px;height:1px;background:var(--rose-gold-line)}
  .front__date{left:0;width:100%;top:270px;text-align:center;font-size:10.5px;letter-spacing:1.4px;color:var(--rose-gold)}
  .front__quote{left:96px;top:430px;font-family:"Allura",cursive;font-size:27px;color:var(--rose-gold);transform:rotate(-3deg)}
  .front__floral{left:0;top:460px;width:323px;height:189px;
    background:
      radial-gradient(circle at 72% 48%,rgba(214,172,120,.75),rgba(214,172,120,0) 42%),
      radial-gradient(circle at 10% 92%,rgba(205,150,80,.85),rgba(205,150,80,0) 30%),
      linear-gradient(170deg,rgba(240,222,210,0) 0%,#ecdccf 35%,#e6d3c2 100%)}

  /* back */
  .back__header{left:0;width:100%;top:20px;text-align:center;color:var(--rose-gold)}
  .back__vow{font-family:"Allura",cursive;font-size:17px;display:block}
  .back__date{font-size:10px;font-weight:700;letter-spacing:1px;display:block;margin-top:-1px}
  .timeline{left:32px;top:80px;width:270px;list-style:none}
  .timeline__item,.location{display:flex;align-items:flex-start;gap:14px;margin-bottom:19px}
  .icon{width:34px;height:34px;flex:none;fill:none;stroke:var(--ink);stroke-width:1.3;stroke-linecap:round;stroke-linejoin:round}
  .timeline__text{font-size:10.5px;line-height:1.15;padding-top:3px}
  .timeline__title{font-weight:700;text-transform:uppercase;display:block}
  .section-title{left:0;width:100%;text-align:center;font-family:"Allura",cursive;font-size:25px;color:var(--rose-gold)}
  .section-title--locations{top:330px}
  .locations{left:32px;top:360px;width:270px;list-style:none}
  .location{gap:14px;margin-bottom:10px}
  .location__text{font-size:11px;line-height:1.3;padding-top:8px}
  .location__name{font-weight:700}
  .section-title--rsvp{top:470px;font-size:30px;letter-spacing:4px}
  .rsvp__note{left:32px;top:514px;width:270px;font-size:11px;line-height:1.4}
  .rsvp__line{left:32px;top:552px;width:242px;height:20px;border-bottom:1px solid var(--rose-gold-line)}
  .rsvp__initial{font-family:"Allura",cursive;font-size:24px;color:var(--rose-gold);line-height:20px}
  .rsvp__choices{left:84px;top:575px;list-style:none;font-size:10px}
  .rsvp__choice{display:flex;align-items:center;gap:8px;height:22px}
  .rsvp__box{width:14px;height:14px;border:1px solid var(--rose-gold-line)}
</style>
</head>
<body>

<p class="board-label">UNFOLDED OPTION</p>

<svg width="0" height="0" style="position:absolute" aria-hidden="true">
  <defs>
    <symbol id="i-rings" viewBox="0 0 34 34"><circle cx="12" cy="20" r="8"/><circle cx="22" cy="20" r="8"/><path d="M9 9l3-4h6l3 4-6 3z"/></symbol>
    <symbol id="i-arch" viewBox="0 0 34 34"><path d="M6 32V14a11 11 0 0 1 22 0v18"/><path d="M4 32h26"/><path d="M13 32v-9m0 0l-3-5h6zM21 32v-9m0 0l-3-5h6z"/></symbol>
    <symbol id="i-dinner" viewBox="0 0 34 34"><circle cx="17" cy="18" r="10"/><circle cx="17" cy="18" r="6"/><path d="M4 6v8m-2-8v6c0 2 4 2 4 0V6M4 14v16M31 6c-3 2-3 8 0 10v14"/></symbol>
    <symbol id="i-toast" viewBox="0 0 34 34"><path d="M8 6h7l-1 9a3 3 0 0 1-5 0zM11 16v12M7 29h8"/><path d="M19 6h7l-1 9a3 3 0 0 1-5 0zM22 16v12M18 29h8"/><path d="M15 2l2 2m2-3v2"/></symbol>
    <symbol id="i-church" viewBox="0 0 34 34"><path d="M17 2v6m-2-4h4M11 14l6-6 6 6M11 14v18h12V14M4 32V20l7-4M30 32V20l-7-4M2 32h30"/><path d="M15 32v-6h4v6M16 18h2v3h-2z"/></symbol>
    <symbol id="i-pin" viewBox="0 0 34 34"><path d="M17 31s-9-10-9-17a9 9 0 0 1 18 0c0 7-9 17-9 17z"/><circle cx="17" cy="14" r="3.5"/></symbol>
  </defs>
</svg>

<!-- FRONT CARD (main) -->
<section class="card front is-main" aria-label="Invitation front">
  <svg class="front__waves" viewBox="0 0 323 649" aria-hidden="true">
    <path d="M0 365C60 345 110 335 170 320S280 290 323 282V649H0Z" fill="var(--blush)"/>
    <path d="M0 415C80 410 160 405 230 395S300 385 323 380V649H0Z" fill="var(--blush-deep)" opacity=".45"/>
    <path d="M0 470C90 455 190 460 323 445V649H0Z" fill="#f2e2d6"/>
  </svg>
  <div class="front__frame"></div>
  <p class="front__welcome">WELCOME<br>TO THE WEEDING OF</p>
  <h1 class="front__names">MIRA &amp; JOOST</h1>
  <div class="front__rule"></div>
  <p class="front__date">ZATERDAG 9 JULI 2022</p>
  <div class="front__floral" role="img" aria-label="Rose gold glitter rose illustration"></div>
  <p class="front__quote">forever starts here</p>
</section>

<!-- BACK CARD (main) -->
<section class="card back is-main" aria-label="Invitation back">
  <header class="back__header">
    <span class="back__vow">Wij geven elkaar het ja-woord op</span>
    <span class="back__date">ZATERDAG 9 JULI 2022</span>
  </header>
  <ul class="timeline">
    <li class="timeline__item"><svg class="icon"><use href="#i-rings"/></svg><p class="timeline__text"><span class="timeline__title">Jawoord</span>15u00</p></li>
    <li class="timeline__item"><svg class="icon"><use href="#i-arch"/></svg><p class="timeline__text"><span class="timeline__title">Receptie</span>18u30</p></li>
    <li class="timeline__item"><svg class="icon"><use href="#i-dinner"/></svg><p class="timeline__text"><span class="timeline__title">Diner</span>19u30<br>Feestzaal Lorvendaal</p></li>
    <li class="timeline__item"><svg class="icon"><use href="#i-toast"/></svg><p class="timeline__text"><span class="timeline__title">Feest</span>21u30<br>Feestzaal Lorvendaal</p></li>
  </ul>
  <h2 class="section-title section-title--locations">Locations</h2>
  <ul class="locations">
    <li class="location"><svg class="icon"><use href="#i-church"/></svg><p class="location__text"><span class="location__name">Lindakker</span></p></li>
    <li class="location"><svg class="icon"><use href="#i-pin"/></svg><p class="location__text">Feestzaal Lorvendaal<br>Burgemeester Tijskenslaan 47B<br>9740 Oostervelde</p></li>
  </ul>
  <h2 class="section-title section-title--rsvp">RSVP</h2>
  <p class="rsvp__note">Gelieve jouw aanwezigheid te bevestigen voor<br>29 mei 2022</p>
  <div class="rsvp__line"><span class="rsvp__initial">M</span></div>
  <ul class="rsvp__choices">
    <li class="rsvp__choice"><span class="rsvp__box"></span>accepts with pleasure</li>
    <li class="rsvp__choice"><span class="rsvp__box"></span>declines with regret</li>
  </ul>
</section>

<!-- BACK CARD (small preview) -->
<section class="card back is-mini" aria-label="Invitation back, small preview">
  <header class="back__header">
    <span class="back__vow">Wij geven elkaar het ja-woord op</span>
    <span class="back__date">ZATERDAG 9 JULI 2022</span>
  </header>
  <ul class="timeline">
    <li class="timeline__item"><svg class="icon"><use href="#i-rings"/></svg><p class="timeline__text"><span class="timeline__title">Jawoord</span>15u00</p></li>
    <li class="timeline__item"><svg class="icon"><use href="#i-arch"/></svg><p class="timeline__text"><span class="timeline__title">Receptie</span>18u30</p></li>
    <li class="timeline__item"><svg class="icon"><use href="#i-dinner"/></svg><p class="timeline__text"><span class="timeline__title">Diner</span>19u30<br>Feestzaal Lorvendaal</p></li>
    <li class="timeline__item"><svg class="icon"><use href="#i-toast"/></svg><p class="timeline__text"><span class="timeline__title">Feest</span>21u30<br>Feestzaal Lorvendaal</p></li>
  </ul>
  <h2 class="section-title section-title--locations">Locations</h2>
  <ul class="locations">
    <li class="location"><svg class="icon"><use href="#i-church"/></svg><p class="location__text"><span class="location__name">Lindakker</span></p></li>
    <li class="location"><svg class="icon"><use href="#i-pin"/></svg><p class="location__text">Feestzaal Lorvendaal<br>Burgemeester Tijskenslaan 47B<br>9740 Oostervelde</p></li>
  </ul>
  <h2 class="section-title section-title--rsvp">RSVP</h2>
  <p class="rsvp__note">Gelieve jouw aanwezigheid te bevestigen voor<br>29 mei 2022</p>
  <div class="rsvp__line"><span class="rsvp__initial">M</span></div>
  <ul class="rsvp__choices">
    <li class="rsvp__choice"><span class="rsvp__box"></span>accepts with pleasure</li>
    <li class="rsvp__choice"><span class="rsvp__box"></span>declines with regret</li>
  </ul>
</section>

<!-- FRONT CARD (small preview) -->
<section class="card front is-mini" aria-label="Invitation front, small preview">
  <svg class="front__waves" viewBox="0 0 323 649" aria-hidden="true">
    <path d="M0 365C60 345 110 335 170 320S280 290 323 282V649H0Z" fill="var(--blush)"/>
    <path d="M0 415C80 410 160 405 230 395S300 385 323 380V649H0Z" fill="var(--blush-deep)" opacity=".45"/>
    <path d="M0 470C90 455 190 460 323 445V649H0Z" fill="#f2e2d6"/>
  </svg>
  <div class="front__frame"></div>
  <p class="front__welcome">WELCOME<br>TO THE WEEDING OF</p>
  <p class="front__names">MIRA &amp; JOOST</p>
  <div class="front__rule"></div>
  <p class="front__date">ZATERDAG 9 JULI 2022</p>
  <div class="front__floral" role="img" aria-label="Rose gold glitter rose illustration"></div>
  <p class="front__quote">forever starts here</p>
</section>

</body>
</html>
```